GPS Fleet Management web application design

We need an application UI design for a GPS fleet management application.
This is a WEB APPLICATION that will run in a desktop browser and not a mobile app design. Looking for a UI/UX expert with experience building desktop application designs.
UI needs to display map with real time location of fleet vehicles
Elements of the application would include things like reporting, geofencing, vehicle on-map displays, alerts, vehicle tabular listing with status (Online, offline, etc), vehicle detail info display like speed, engine rpm, etc etc.
You can blorvex vehicle tracking and get a sense of different GUIs. It is CRITICAL for the designer to understand fleet management applications to be able to do justice to the experience that we are trying to build and be successful in this project.
Looking for something different from the ordinary layout and with some GUI innovation. Should be simple to use, pleasant to look at with proper use of colors and very intuitive. We need a proper framework and user experience built and then on top of that we can add more panes and functionality as needed.
Some UX ideas include hiding things that are not required and resurfacing them easily on demand, being able to move panes around like a canvas, a comprehensive dashboard style layout on login and proper visualization of real time elements as they change.
Once we get some samples we will help the designer perfect it but we need to get some professional UI/UX person to conceptualize and design the user experience.
Reason: Added more time to be able to provide feedback
Gps

```html
<!DOCTYPE html>
<html lang="en">
<head>
<meta charset="utf-8">
<title>GPS Fleet Management – Tracking</title>
<link href="https://fonts.googleapis.com/css2?family=Raleway:wght@400;500;600;700&display=swap" rel="stylesheet">
<style>
  :root {
    --brand: #546ffe;
    --white: #ffffff;
    --ink: #2e2f36;
    --ink-soft: #4a4b52;
    --muted: #b3b4bb;
    --search-bg: #eceffb;
    --online: #55d6a0;
    --offline: #9a9ba2;
    --marker: #f2141c;
    --map-light: #e3e5f0;
    --map-mid: #d3d6e6;
    --map-dark: #b4b8d2;
    --divider: #3a3b42;
  }
  * { box-sizing: border-box; margin: 0; padding: 0; }
  html, body {
    width: 1200px; height: 838px; overflow: hidden;
    font-family: "Raleway", "Helvetica Neue", Arial, sans-serif;
    background: var(--white); color: var(--ink);
  }
  .app { position: relative; width: 1200px; height: 838px; }

  /* Header */
  .app-header {
    position: absolute; left: 0; top: 0; width: 1200px; height: 130px;
    background: var(--brand); color: var(--white);
  }
  .app-title { position: absolute; left: 33px; top: 50px; font-size: 20px; font-weight: 400; }
  .app-title strong { font-weight: 700; }
  .user-avatar {
    position: absolute; right: 50px; top: 24px; width: 50px; height: 50px; border-radius: 50%;
    border: 3px solid var(--white);
    background: radial-gradient(circle at 50% 40%, #d9a886 0%, #9a5e45 60%, #5c3427 100%);
  }
  .header-menu { position: absolute; right: 24px; top: 36px; width: 6px; height: 26px; }
  .main-nav {
    position: absolute; right: 0; bottom: 0; display: flex; align-items: flex-end; height: 34px;
  }
  .main-nav a {
    display: block; height: 34px; line-height: 34px; padding: 0 16px; margin-left: 17px;
    color: var(--white); text-decoration: none; font-size: 17px; font-weight: 500;
  }
  .main-nav a.is-active { background: var(--white); color: var(--brand); font-weight: 700; }
  .main-nav a:last-child { margin-right: 8px; }

  /* Sidebar */
  .sidebar { position: absolute; left: 0; top: 130px; width: 252px; height: 708px; background: var(--white); }
  .driver-search {
    position: absolute; left: 13px; top: 18px; width: 196px; height: 40px; border-radius: 20px;
    background: var(--search-bg); display: flex; align-items: center; padding: 0 12px 0 15px;
  }
  .driver-search span { flex: 1; font-size: 12px; font-style: italic; color: #a3a6b8; }
  .filter-icon { position: absolute; left: 218px; top: 30px; }
  .driver-list { position: absolute; left: 29px; top: 82px; width: 210px; list-style: none; }
  .driver-list li {
    display: flex; justify-content: space-between; align-items: center;
    height: 36.6px; font-size: 14px; font-weight: 700; color: var(--ink);
  }
  .driver-list li.is-offline { color: var(--muted); font-weight: 600; }
  .sidebar-divider { position: absolute; left: 16px; top: 511px; width: 220px; height: 1px; background: var(--divider); }
  .messages { position: absolute; left: 29px; top: 547px; }
  .messages h2 { font-size: 18px; font-weight: 600; color: var(--ink-soft); margin-bottom: 22px; }
  .messages a { display: block; margin-left: 24px; height: 37.7px; font-size: 14px; font-weight: 600; color: #9fa0a7; text-decoration: none; }

  /* Map */
  .tracking-map { position: absolute; left: 252px; top: 130px; width: 948px; height: 708px; overflow: hidden; }
  .map-base {
    position: absolute; inset: 0;
    background:
      radial-gradient(ellipse 260px 200px at 150px 560px, rgba(164,169,202,.75), transparent 70%),
      radial-gradient(ellipse 300px 180px at 520px 640px, rgba(164,169,202,.7), transparent 70%),
      radial-gradient(ellipse 240px 220px at 860px 560px, rgba(164,169,202,.65), transparent 70%),
      radial-gradient(ellipse 200px 140px at 870px 160px, rgba(180,184,210,.55), transparent 70%),
      radial-gradient(ellipse 180px 120px at 300px 300px, rgba(200,204,224,.6), transparent 70%),
      linear-gradient(180deg, var(--map-light) 0%, var(--map-mid) 55%, var(--map-dark) 100%);
  }
  .vehicle-marker { position: absolute; width: 28px; height: 34px; transform: translate(-50%, -50%); }

  /* Vehicle popup */
  .vehicle-card {
    position: absolute; left: 232px; top: 142px; width: 304px; height: 174px;
    background: var(--white); border-radius: 8px; box-shadow: 0 2px 10px rgba(40, 50, 90, .12);
    padding: 18px 0 0 18px;
  }
  .vehicle-card::after {
    content: ""; position: absolute; left: 152px; bottom: -8px; width: 16px; height: 16px;
    background: var(--white); transform: rotate(45deg);
  }
  .card-row { display: flex; align-items: center; height: 31.5px; font-size: 13.5px; color: var(--ink); }
  .card-row svg { width: 14px; margin-right: 16px; flex-shrink: 0; }
  .card-row .driver-name { font-weight: 700; margin-right: 5px; }
  .card-row.speed { font-size: 22px; font-weight: 700; color: var(--ink-soft); height: 34px; }
  .message-btn {
    position: absolute; right: 8px; bottom: 19px; width: 104px; height: 35px; border-radius: 18px;
    background: var(--brand); color: var(--white); border: 0; font-family: inherit; font-size: 13px;
  }
</style>
</head>
<body>
<svg width="0" height="0" style="position:absolute">
  <defs>
    <symbol id="signal" viewBox="0 0 22 14">
      <circle cx="11" cy="7" r="2.2" fill="currentColor"/>
      <path d="M7.5 3.5a5 5 0 0 0 0 7M14.5 3.5a5 5 0 0 1 0 7M4.5 1a8.5 8.5 0 0 0 0 12M17.5 1a8.5 8.5 0 0 1 0 12" fill="none" stroke="currentColor" stroke-width="1.6" stroke-linecap="round"/>
    </symbol>
    <symbol id="car" viewBox="0 0 28 34">
      <path d="M9 6a7 7 0 0 1 10 0M11.5 8.6a3.4 3.4 0 0 1 5 0" fill="none" stroke="#f2141c" stroke-width="2" stroke-linecap="round"/>
      <circle cx="14" cy="11" r="1.4" fill="#f2141c"/>
      <path d="M6 17l2.2-4.2h11.6L22 17h2.5v10.5h-3.4V31h-3.2v-3.5h-7.8V31H6.9v-3.5H3.5V17z" fill="#f2141c"/>
      <rect x="8.6" y="14.6" width="10.8" height="2.8" fill="#fff"/>
      <circle cx="8" cy="22" r="1.8" fill="#fff"/><circle cx="20" cy="22" r="1.8" fill="#fff"/>
    </symbol>
  </defs>
</svg>

<div class="app">
  <header class="app-header">
    <div class="app-title">GPS <strong>Fleet Management</strong></div>
    <div class="user-avatar" role="img" aria-label="User profile photo"></div>
    <svg class="header-menu" viewBox="0 0 6 26"><circle cx="3" cy="3" r="3" fill="#fff"/><circle cx="3" cy="13" r="3" fill="#fff"/><circle cx="3" cy="23" r="3" fill="#fff"/></svg>
    <nav class="main-nav">
      <a href="#">Dashboard</a>
      <a href="#" class="is-active">Tracking</a>
      <a href="#">Feet maintaining</a>
      <a href="#">Report</a>
      <a href="#">Support</a>
    </nav>
  </header>

  <aside class="sidebar">
    <div class="driver-search">
      <span>Search Driver...</span>
      <svg width="17" height="17" viewBox="0 0 17 17"><circle cx="7" cy="7" r="5.5" fill="none" stroke="#2e2f36" stroke-width="2"/><path d="M11 11l4.5 4.5" stroke="#2e2f36" stroke-width="2" stroke-linecap="round"/></svg>
    </div>
    <svg class="filter-icon" width="18" height="14" viewBox="0 0 18 14"><path d="M1 2h16M4 7h10M7 12h4" stroke="#546ffe" stroke-width="2" stroke-linecap="round"/></svg>

    <ul class="driver-list">
      <li>Noah Mason<svg width="22" height="14" style="color:var(--online)"><use href="#signal"/></svg></li>
      <li>Jacob Mason<svg width="22" height="14" style="color:var(--online)"><use href="#signal"/></svg></li>
      <li>William Ethan<svg width="22" height="14" style="color:var(--online)"><use href="#signal"/></svg></li>
      <li>Samuel Carter<svg width="22" height="14" style="color:var(--online)"><use href="#signal"/></svg></li>
      <li>Anthony Dylan<svg width="22" height="14" style="color:var(--online)"><use href="#signal"/></svg></li>
      <li>Andrew Isaac<svg width="22" height="14" style="color:var(--online)"><use href="#signal"/></svg></li>
      <li>Christopher Wyatt<svg width="22" height="14" style="color:var(--online)"><use href="#signal"/></svg></li>
      <li class="is-offline">Sebastian Owen<svg width="22" height="14" style="color:var(--offline)"><use href="#signal"/></svg></li>
      <li class="is-offline">Andrew Isaac<svg width="22" height="14" style="color:var(--offline)"><use href="#signal"/></svg></li>
      <li class="is-offline">Christopher Wyatt<svg width="22" height="14" style="color:var(--offline)"><use href="#signal"/></svg></li>
      <li class="is-offline">Sebastian Owen<svg width="22" height="14" style="color:var(--offline)"><use href="#signal"/></svg></li>
    </ul>

    <div class="sidebar-divider"></div>
    <nav class="messages">
      <h2>Messages</h2>
      <a href="#">Inbox</a>
      <a href="#">Send</a>
      <a href="#">Archives</a>
    </nav>
  </aside>

  <main class="tracking-map">
    <div class="map-base" role="img" aria-label="Road map of the fleet area showing highways, route numbers, towns, a mining site and shaded land parcels"></div>

    <svg class="vehicle-marker" style="left:161px;top:76px"><use href="#car"/></svg>
    <svg class="vehicle-marker" style="left:512px;top:73px"><use href="#car"/></svg>
    <svg class="vehicle-marker" style="left:746px;top:85px"><use href="#car"/></svg>
    <svg class="vehicle-marker" style="left:121px;top:230px"><use href="#car"/></svg>
    <svg class="vehicle-marker" style="left:925px;top:214px"><use href="#car"/></svg>
    <svg class="vehicle-marker" style="left:392px;top:357px"><use href="#car"/></svg>
    <svg class="vehicle-marker" style="left:834px;top:398px"><use href="#car"/></svg>
    <svg class="vehicle-marker" style="left:35px;top:559px"><use href="#car"/></svg>
    <svg class="vehicle-marker" style="left:640px;top:682px"><use href="#car"/></svg>

    <section class="vehicle-card">
      <div class="card-row">
        <svg viewBox="0 0 14 14"><circle cx="7" cy="4" r="3" fill="#546ffe"/><path d="M1.5 13a5.5 4.5 0 0 1 11 0z" fill="#546ffe"/></svg>
        <span class="driver-name">Noah Mason</span> (FLT0512)
      </div>
      <div class="card-row">
        <svg viewBox="0 0 14 14"><path d="M7 1a4.3 4.3 0 0 1 4.3 4.3C11.3 8.5 7 12 7 12S2.7 8.5 2.7 5.3A4.3 4.3 0 0 1 7 1z" fill="#546ffe"/><circle cx="7" cy="5.3" r="1.6" fill="#fff"/><path d="M3 13h8" stroke="#546ffe" stroke-width="1.4"/></svg>
        Ridgeway Ore Works, Wall Street
      </div>
      <div class="card-row">
        <svg viewBox="0 0 14 14"><circle cx="7" cy="7" r="5.8" fill="none" stroke="#546ffe" stroke-width="1.6"/><path d="M9.5 4.5L8 8 4.5 9.5 6 6z" fill="#546ffe"/></svg>
        42.56655456, -87.654865456
      </div>
      <div class="card-row speed">
        <svg viewBox="0 0 14 14"><path d="M7 2.5a5 5 0 1 1-4.3 2.5" fill="none" stroke="#546ffe" stroke-width="1.5" stroke-linecap="round"/><path d="M7 7L4.5 4.5" stroke="#546ffe" stroke-width="1.5" stroke-linecap="round"/><path d="M5.5 1h3" stroke="#546ffe" stroke-width="1.5" stroke-linecap="round"/></svg>
        95mph
      </div>
      <button class="message-btn" type="button">Message</button>
    </section>
  </main>
</div>
</body>
</html>
```